Letterhead to Prospective Clients

Create a letterhead (word & canva) that I will use to send letters to prospective clients and also include the Coralwood Estate Partners Logo, My Contact Details and Interchangeable "Suburb". Use the same font and colour pallete

Maris Dulworth | "Suburb" Specialist - Kestrelvale & Surrounds
Mobile: 0417 862 095
Email: MD@CoralwoodEstatePartners.com.au

```html
<!DOCTYPE html>
<html lang="en">
<head>
<meta charset="utf-8">
<title>Coralwood Estate Partners – Letterhead</title>
<link href="https://fonts.googleapis.com/css2?family=Montserrat:wght@300;400;500;600&display=swap" rel="stylesheet">
<style>
  :root{
    --backdrop:#818287;
    --paper:#ffffff;
    --tan:#D4A67E;
    --slate:#4D5669;
    --ink:#5a5f6b;
    --rule:#9a9ca3;
  }
  *{margin:0;padding:0;box-sizing:border-box}
  html,body{width:1200px;height:1200px;overflow:hidden;background:var(--backdrop)}
  body{font-family:"Montserrat",sans-serif;position:relative}
  .letterhead{
    position:absolute;left:175px;top:50px;width:850px;height:1100px;
    background:var(--paper);
  }
  .accent-block{position:absolute;left:0;top:54px;width:112px;height:52px;background:var(--tan)}
  .brand-name{
    position:absolute;left:120px;top:52px;width:200px;
    font-weight:400;font-size:17px;line-height:1.3;letter-spacing:1.6px;
    text-transform:uppercase;color:var(--slate);text-align:center;
  }
  .agent-band{
    position:absolute;left:330px;top:54px;right:0;height:52px;background:var(--slate);
    color:#fff;text-align:right;padding:8px 64px 0 0;
  }
  .agent-name{font-weight:600;font-size:15px;letter-spacing:2.4px;text-transform:uppercase;line-height:20px}
  .agent-area{font-weight:400;font-size:10px;line-height:14px}
  .footer-rule{position:absolute;left:102px;width:646px;top:1006px;height:1px;background:var(--rule)}
  .contact-row{
    position:absolute;left:102px;width:646px;top:1018px;
    display:flex;justify-content:space-between;align-items:center;
    font-size:10.6px;color:var(--ink);letter-spacing:.2px;white-space:nowrap;
  }
  .contact-item{display:flex;align-items:center;gap:4px}
  .contact-icon{width:14px;height:14px;flex:none}
  .base-band{position:absolute;left:0;right:0;bottom:0;height:52px;background:var(--slate)}
</style>
</head>
<body>
  <main class="letterhead">
    <div class="accent-block"></div>
    <div class="brand-name">Coralwood<br>Estate Partners</div>
    <div class="agent-band">
      <div class="agent-name">Maris Dulworth</div>
      <div class="agent-area">"Suburb" Specialist - Kestrelvale &amp; Surrounds</div>
    </div>

    <div class="footer-rule"></div>
    <div class="contact-row">
      <span class="contact-item">
        <svg class="contact-icon" viewBox="0 0 16 16" aria-hidden="true"><circle cx="8" cy="8" r="7" fill="none" stroke="#D4A67E" stroke-width="1.2"/><rect x="5.6" y="3.8" width="4.8" height="8.4" rx="1" fill="none" stroke="#D4A67E" stroke-width="1"/><circle cx="8" cy="10.6" r=".6" fill="#D4A67E"/></svg>
        0417 862 095
      </span>
      <span class="contact-item">
        <svg class="contact-icon" viewBox="0 0 16 16" aria-hidden="true"><circle cx="8" cy="8" r="7" fill="none" stroke="#D4A67E" stroke-width="1.2"/><rect x="4" y="5.2" width="8" height="5.6" fill="none" stroke="#D4A67E" stroke-width="1"/><path d="M4 5.2 8 8.4 12 5.2" fill="none" stroke="#D4A67E" stroke-width="1"/></svg>
        MD@CoralwoodEstatePartners.com.au
      </span>
      <span class="contact-item">
        <svg class="contact-icon" viewBox="0 0 16 16" aria-hidden="true"><circle cx="8" cy="8" r="7" fill="none" stroke="#D4A67E" stroke-width="1.2"/><path d="M4 8 8 4.4 12 8V11.6H4Z" fill="#D4A67E"/><rect x="7" y="9" width="2" height="2.6" fill="#fff"/></svg>
        Marlow Hills, Kestrel Bay, Fernleigh &amp; Mt Ashby
      </span>
    </div>
    <div class="base-band"></div>
  </main>
</body>
</html>
```